Bright Paddock Learning Program with the aim of promoting a skills football to school aged children to

Need an A5 back to front one page brochure which is colourful, fun and active to attract the students to purchase the football with part of the funds going back to the school.
Whole idea is to get more footballs in the hands of children of primary school age, fo the school to earn funds from the sale as well as us also making some funds from the sale.
Target Market(s)
5-11 Year old boys and girls
Industry/Entity Type
School
Colors
219ed3
ffffff
0255a3
33b8a4
ec1f27
Requirements
Must have
- Must have football, price, promotional words as per example and contact details of who is ordering the footballs.
- Have included a version we have done up but are not happy with, needs to be much more professional than the attachment to the brief.
Nice to have
- Promotional component on the front with plenty of colours and attraction, with detail requirements on the back
Should not have
- No soccer or KRB balls, only Aussie Rules Footballs in design

```html
<!DOCTYPE html>
<html lang="en">
<head>
<meta charset="utf-8">
<title>Football for School – Bright Paddock Learning Program</title>
<link href="https://fonts.googleapis.com/css2?family=Anton&family=Roboto+Condensed:ital,wght@0,400;0,700;1,700;1,900&display=swap" rel="stylesheet">
<style>
  :root{
    --stage:#1c1d1f;
    --grass-light:#3f9a45;
    --grass-dark:#1d5e2a;
    --night:#101712;
    --accent-green:#3db54a;
    --ball-red:#ec1f27;
    --ball-pink:#f25a6a;
    --white:#ffffff;
    --ink:#1a1a1a;
  }
  *{margin:0;padding:0;box-sizing:border-box}
  html,body{width:1200px;height:848px;overflow:hidden;background:var(--stage)}
  .flyer{
    position:absolute;left:300px;top:0;width:600px;height:848px;
    overflow:hidden;background:var(--night);
    font-family:"Roboto Condensed",Arial,sans-serif;color:var(--white);
  }
  .grass{
    position:absolute;left:0;top:0;width:600px;height:520px;
    background:radial-gradient(ellipse at 70% 30%,var(--grass-light),var(--grass-dark) 80%);
  }
  .lower-art,.ball-photo{position:absolute;left:0;top:0;width:600px;height:848px}
  .title{
    position:absolute;right:18px;top:24px;text-align:right;
    font-family:"Anton",Impact,sans-serif;line-height:.95;text-transform:uppercase;
  }
  .title .main{display:block;font-size:84px;letter-spacing:1px}
  .title .sub{display:block;font-size:58px;letter-spacing:1px}
  .tagline{
    position:absolute;left:318px;top:232px;width:282px;
    padding:14px 14px 14px 22px;background:rgba(10,20,12,.88);
    border-radius:22px 0 0 22px;
    font-weight:900;font-style:italic;font-size:19px;line-height:1.2;
  }
  .price{position:absolute;left:318px;top:440px;width:266px;height:220px}
  .price .amount{
    position:absolute;right:0;top:0;
    font-family:"Anton",Impact,sans-serif;font-size:196px;line-height:1;color:var(--white);
  }
  .price .band{
    position:absolute;left:-6px;right:-10px;top:96px;height:52px;background:var(--accent-green);
    opacity:.92;
  }
  .price .label{
    position:absolute;left:8px;top:90px;
    font-family:"Anton",Impact,sans-serif;font-size:52px;line-height:1;color:var(--night);
    letter-spacing:1px;
  }
  .order-form{
    position:absolute;left:22px;top:676px;width:556px;height:130px;
    background:var(--white);border:4px solid var(--accent-green);
    color:var(--ink);padding:10px 16px;font-size:12px;
  }
  .order-form h2{font-size:13px;font-weight:700;text-transform:uppercase;margin-bottom:6px}
  .order-form .row{display:flex;gap:18px;align-items:flex-end;margin-bottom:7px}
  .field{display:flex;align-items:flex-end;gap:6px;flex:1}
  .field .line{flex:1;border-bottom:1px solid #555;height:12px}
  .check{display:inline-flex;align-items:center;gap:4px;margin-right:14px}
  .check i{width:11px;height:11px;border:1px solid #333;display:inline-block}
  .office{font-size:10px;text-transform:uppercase;color:#444}
  .footnote{
    position:absolute;left:22px;top:814px;font-size:11px;font-style:italic;font-weight:700;
  }
</style>
</head>
<body>
  <main class="flyer">
    <div class="grass" role="img" aria-label="Close-up of green grass turf"></div>

    <svg class="lower-art" viewBox="0 0 600 848" aria-hidden="true">
      <path d="M0 470 C180 430 400 420 600 470 L600 848 L0 848 Z" fill="#101712"/>
      <path d="M240 455 C380 432 500 440 600 468 L600 490 C500 460 380 452 240 455 Z" fill="#3db54a"/>
    </svg>

    <svg class="ball-photo" viewBox="0 0 600 848" role="img" aria-label="Close-up photo of a red oval Aussie Rules football with white laces, tilted diagonally">
      <defs>
        <radialGradient id="ballTone" cx="45%" cy="45%" r="60%">
          <stop offset="0" stop-color="#f25a6a"/>
          <stop offset=".6" stop-color="#ec1f27"/>
          <stop offset="1" stop-color="#b5121b"/>
        </radialGradient>
      </defs>
      <g transform="translate(90 330) rotate(-62)">
        <path d="M-450 0 C-300 -215 300 -215 450 0 C300 215 -300 215 -450 0 Z" fill="url(#ballTone)"/>
      </g>
    </svg>

    <h1 class="title"><span class="main">Football</span><span class="sub">For School</span></h1>

    <p class="tagline">Order your own exclusive* 12" Skill Football in your local CRFL club colours</p>

    <div class="price">
      <span class="amount">$70</span>
      <span class="band"></span>
      <span class="label">JUST EACH</span>
    </div>

    <section class="order-form">
      <h2>Order Information</h2>
      <div class="row">
        <div class="field">Student Name:<span class="line"></span></div>
        <div class="field">Classroom:<span class="line"></span></div>
      </div>
      <div class="row">
        <div class="field">Year:<span class="line"></span></div>
        <div class="field">Number of footballs:<span class="line"></span></div>
      </div>
      <div class="row">
        <span>Payment method:</span>
        <span class="check"><i></i>Cash</span>
        <span class="check"><i></i>Cheque</span>
        <span class="check"><i></i>EFT</span>
      </div>
      <div class="row">
        <div class="field"><span class="office">Office only – Payment received:</span><span class="line"></span></div>
      </div>
    </section>

    <p class="footnote">*offer only available at selected schools</p>
  </main>
</body>
</html>
```